Wordpress Design Project (Tobwin)

We need a wordpress design for an established auction and real estate company based in Virginia. The winning design will incorporate the colors of logo (red and black) creatively with an accent color in a very professional and clean layout.

Industry/Entity Type

Real Estate

Requirements
Must have
• We will require winning designer to provide a layered PSD (Adobe photoshop) concept file, along with any non-standard font files used.

Horizontal Navigation menu with these links:
Home - Upcoming Auctions - Past Auctions - For Sale- Consignments - About Us - Highlights - Contact Us

A slideshow element on the home page using the placeholder image provided.

Sidebar widgets to be included are: Email sign-up form - Featured Auctions - Featured Assets for Sale (see attached for visual of these widgets)

attached logos in footer with company contact info

```html
<!DOCTYPE html>
<html lang="en">
<head>
<meta charset="utf-8">
<title>Tobwin Enterprises</title>
<link rel="stylesheet" href="https://fonts.googleapis.com/css2?family=Open+Sans:wght@400;600;700&family=Arimo:wght@400;700&display=swap">
<style>
:root{
  --red:#e0261c;
  --red-dark:#c81e15;
  --black:#1a0604;
  --nav:#2a0906;
  --ink:#555;
  --text:#444;
  --paper:#f4f4f4;
  --white:#fff;
  --line:#d6d6d6;
  --gold:#f2b71a;
}
*{box-sizing:border-box;margin:0;padding:0}
html,body{width:973px;height:1200px;overflow:hidden}
body{position:relative;background:var(--paper);font-family:"Arimo",Arial,sans-serif;color:var(--text)}
.abs{position:absolute}
/* header */
.brand{left:89px;top:26px;display:flex;align-items:center;gap:8px}
.brand-mark{width:22px;height:22px;background:var(--red)}
.brand-name{font-family:"Open Sans",sans-serif;font-weight:700;font-size:30px;color:var(--black);line-height:1}
.brand-name small{display:block;font-size:10px;letter-spacing:5px;color:var(--red);font-weight:600;margin-top:2px}
.call{left:596px;top:38px;text-align:center;font-family:"Open Sans",sans-serif}
.call h4,.follow h4{font-size:17px;font-weight:600;color:#555}
.call p{font-size:19px;color:var(--red);display:flex;align-items:center;gap:8px;margin-top:2px}
.follow{left:772px;top:38px;font-family:"Open Sans",sans-serif}
.social{display:flex;gap:12px;margin-top:6px}
.social span{width:26px;height:26px;background:#555;border-radius:3px}
/* nav */
.nav{left:0;top:102px;width:973px;height:33px;background:var(--nav);border-bottom:3px solid var(--black)}
.nav ul{list-style:none;display:flex;position:absolute;left:90px;top:0;height:33px;align-items:center;gap:0}
.nav li{font-family:"Open Sans",sans-serif;font-size:12.2px;color:var(--white);padding:0 12px;height:25px;line-height:25px}
.nav li.active{background:var(--red);padding:0 3px;margin:0 8px}
.nav li:first-child{padding-left:5px}
.caret{font-size:9px;margin-left:4px}
.hero{left:0;top:140px;width:973px;height:278px;background:var(--red)}
.hero-shadow{left:90px;top:418px;width:760px;height:14px;background:radial-gradient(ellipse at top,rgba(0,0,0,.28),transparent 70%)}
.slider{left:84px;top:152px;width:556px;height:252px;background:var(--white);padding:4px}
.slide{width:100%;height:100%;background:linear-gradient(#dfeaf3 0%,#e9eff2 48%,#5f7a70 53%,#8aa0a8 62%,#a6b6bb 100%);position:relative}
.slide-bar{position:absolute;left:0;bottom:0;width:100%;height:24px;background:rgba(70,40,40,.75);display:flex;gap:7px;align-items:center;padding-left:18px}
.dot{width:12px;height:12px;border-radius:50%;background:var(--white)}
.dot.on{background:var(--red)}
.dropdown{left:162px;top:135px;width:142px;background:var(--red);border-radius:0 0 4px 4px;padding:2px 0 3px}
.dropdown li{list-style:none;font-family:"Open Sans",sans-serif;font-size:10.5px;color:var(--white);height:25px;line-height:25px;padding-left:9px}
.dropdown li.hover{background:var(--black);margin-left:-2px}
.signup{left:650px;top:152px;width:240px;height:252px;background:linear-gradient(#fff,#eee);padding:10px 14px}
.signup h3{display:flex;align-items:center;gap:10px;font-family:"Open Sans",sans-serif;font-weight:400;font-size:19px;color:var(--black)}
.signup h3 em{font-style:normal;color:var(--red)}
.env{width:38px;height:38px;border-radius:50%;background:var(--red);border:3px solid #f3c9c6;display:flex;align-items:center;justify-content:center}
.signup label{display:block;font-family:"Open Sans",sans-serif;font-size:11.5px;color:#222;margin:22px 0 6px 3px}
.signup label.second{margin-top:8px}
.field{width:200px;height:29px;background:var(--red);border-radius:4px;border:1px solid #b51810}
.btn-sub{display:inline-block;margin-top:18px;background:var(--black);color:var(--white);font-family:"Open Sans",sans-serif;font-size:16px;padding:4px 11px;border-radius:4px;letter-spacing:.5px}
/* sidebar */
.widget{left:82px;width:217px;background:var(--paper);border:1px solid #e0e0e0;border-top:5px solid var(--red);box-shadow:0 1px 3px rgba(0,0,0,.1);text-align:center}
.widget h2{background:var(--black);color:var(--white);font-family:"Open Sans",sans-serif;font-weight:400;font-size:17px;height:30px;line-height:30px;letter-spacing:.3px}
.widget .meta{font-size:9.5px;line-height:15px;color:#444}
.widget .meta b{color:var(--red);font-weight:400}
.photo{border:1px solid #ccc}
.w-read{display:inline-block;background:var(--red);color:var(--white);font-size:10px;padding:4px 12px;border-radius:3px}
/* main */
.main-title{font-family:"Arimo",Arial,sans-serif;font-weight:400;font-size:15px;color:#555;text-transform:uppercase}
.main-title em{font-style:normal;color:var(--red)}
.intro{left:325px;top:452px;width:561px}
.intro .rule{border-top:1px dashed #ccc;margin:9px 0 8px}
.intro p{font-size:9.3px;line-height:11.8px;color:#555;margin-bottom:15px;text-align:justify}
.intro p b{color:#555}
.card{left:332px;width:550px;height:168px;background:linear-gradient(#f2f2f2,#fff);border:1px solid #ddd;border-top:3px solid var(--black)}
.card .pic{position:absolute;left:8px;top:29px;width:150px;height:84px;border:1px solid #555}
.card .col{position:absolute;font-size:9.5px;line-height:12px;color:#555}
.card .col b{color:var(--red);font-weight:400;display:block}
.card .divider{position:absolute;left:348px;top:30px;height:88px;border-left:1px dashed #bbb}
.card .foot{position:absolute;left:5px;right:5px;top:134px;border-top:1px dashed #ccc}
.btn-prev{position:absolute;left:45px;top:140px;background:var(--red);color:var(--white);font-weight:700;font-size:9.5px;padding:5px 7px;border-radius:3px}
.fav{position:absolute;left:363px;top:142px;display:flex;align-items:center;gap:8px;font-size:9.5px;color:#444}
/* footer */
.footer{left:0;top:1048px;width:973px;height:152px;background:#0c0c0c;border-top:3px solid var(--red);color:var(--white);font-size:9.8px}
.footer .links{position:absolute;left:75px;top:27px}
.footer .contact{position:absolute;left:75px;top:45px}
.footer .flogo{position:absolute;left:152px;top:75px;display:flex;align-items:center;gap:6px;font-family:"Open Sans",sans-serif;font-weight:700;font-size:19px;color:#cfcfcf;line-height:1}
.footer .flogo small{display:block;font-size:7px;letter-spacing:4px;font-weight:600}
.footer .flogo i{width:16px;height:16px;background:#cfcfcf}
.footer .copy{position:absolute;left:74px;top:117px}
.badges{position:absolute;left:548px;top:50px;display:flex;gap:12px;align-items:center}
.badges span{background:#bdbdbd}
</style>
</head>
<body>

<header>
  <div class="abs brand"><span class="brand-mark"></span><div class="brand-name">Tobwin<small>ENTERPRISES</small></div></div>
  <div class="abs call"><h4>Call us</h4>
    <p><svg width="9" height="22" viewBox="0 0 9 22"><path d="M7 1 H3 Q1 1 1 4 V18 Q1 21 3 21 H7 V17 H4 V5 H7Z" fill="#2a0906"/></svg>143 555 0182</p></div>
  <div class="abs follow"><h4>Follow Us</h4><div class="social"><span></span><span></span><span></span></div></div>
</header>

<nav class="abs nav"><ul>
  <li>Home<span class="caret">⌄</span></li>
  <li class="active">Upcoming Auctions<span class="caret">⌄</span></li>
  <li>Past Auctions<span class="caret">⌄</span></li>
  <li>For Sale<span class="caret">⌄</span></li>
  <li>Consignments<span class="caret">⌄</span></li>
  <li>About Us<span class="caret">⌄</span></li>
  <li>Highlights<span class="caret">⌄</span></li>
  <li>Contact Us</li>
</ul></nav>

<section class="abs hero"></section>
<div class="abs hero-shadow"></div>

<div class="abs slider"><div class="slide" role="img" aria-label="Slideshow photo of a calm river with a wooden boathouse and pier under a pale sky">
  <div class="slide-bar"><span class="dot"></span><span class="dot on"></span><span class="dot"></span></div></div></div>

<ul class="abs dropdown">
  <li>Upcoming Aution 1</li><li>Upcoming Aution 1</li><li class="hover">Upcoming Aution 1</li><li>Upcoming Aution 1</li><li>Upcoming Aution 1</li>
</ul>

<aside class="abs signup">
  <h3><span class="env"><svg width="18" height="13" viewBox="0 0 18 13"><rect x="1" y="1" width="16" height="11" fill="#fff" stroke="#2a0906"/><path d="M1 1 L9 7 L17 1" fill="none" stroke="#2a0906"/></svg></span><span><em>Email</em> sign-up</span></h3>
  <label>Your Name</label><div class="field"></div>
  <label class="second">Your Email Address</label><div class="field" style="margin-left:2px"></div>
  <span class="btn-sub">Subscribe Now</span>
</aside>

<aside class="abs widget" style="top:443px;height:289px">
  <h2>Featured Auctions</h2>
  <p class="meta" style="font-weight:700;color:#555;margin:14px 8px 4px;font-size:9.8px">Session 1 : Multi Estate &amp; Consignment Auction</p>
  <div class="photo" role="img" aria-label="Photo of a large white two-storey house with a car in the driveway" style="width:136px;height:90px;margin:0 auto 12px;background:linear-gradient(#8fb5e0,#e6e6e2 45%,#7d8c60)"></div>
  <p class="meta"><b>Start Date / Time :</b> wedneday,<br>Aprail 10,2013 at 2pm</p>
  <p class="meta" style="margin-top:8px"><b>Location :</b> 1180 Alder Creek Lane,<br>Ridgefield, VA23001</p>
  <p class="meta" style="color:#ddd;margin-top:10px">Read More</p>
</aside>

<aside class="abs widget" style="top:740px;height:288px">
  <h2>Featured Assets for Sale</h2>
  <div class="photo" role="img" aria-label="Photo of a green and yellow vintage farm tractor on grass" style="width:136px;height:90px;margin:32px auto 16px;background:linear-gradient(#f4f6f0,#4f8a2c 60%,#3a6d1f)"></div>
  <p class="meta"><b>Start Date / Time :</b> wedneday,<br>Aprail 10,2013 at 2pm</p>
  <p class="meta" style="margin-top:8px"><b>Location :</b> 1180 Alder Creek Lane,<br>Ridgefield, VA23001</p>
  <span class="w-read" style="margin-top:12px">Read More</span>
</aside>

<main>
  <section class="abs intro">
    <h1 class="main-title">Welcome to <em>Tobwin Enterprises</em></h1>
    <div class="rule"></div>
    <p><b>Lorem Ipsum is simply dummy text of the printing and typesetting industry.</b> Lorem Ipsum has been the industry's standard dummy text ever since the 1500s, when an unknown printer took a galley of type and scrambled it to make a type specimen book. It has survived not only five centuries, but also the leap into electronic typesetting, remaining essentially unchanged. It was popularised in the 1960s with the release of Typeline sheets containing Lorem Ipsum passages, and more recently with desktop publishing software like Folio PageSetter including versions of Lorem Ipsum.</p>
    <p>Lorem Ipsum is simply dummy text of the printing and typesetting industry. Lorem Ipsum has been the industry's standard dummy text ever since the 1500s, when an unknown printer took a galley of type and scrambled it to make a type specimen book. It has survived not only five centuries, but also the leap into electronic typesetting, remaining essentially unchanged.</p>
  </section>

  <h2 class="abs main-title" style="left:333px;top:627px">Upcoming <em>Auctions</em></h2>

  <article class="abs card" style="top:659px">
    <div class="pic" role="img" aria-label="Photo of a silver classic sports car parked at an outdoor car show" style="background:linear-gradient(#b9d0e6,#9ea4a8 45%,#c9c9c9 65%,#6f7a62)"></div>
    <div class="col" style="left:168px;top:35px"><b>Title</b><br>Kestrel 4WD &amp; Commercial<br>Vehicles (107)</div>
    <div class="divider"></div>
    <div class="col" style="left:362px;top:35px"><b>Start Date / Time</b><br>Tue 09 April, 10:00 AM<br><b style="margin-top:8px">Location</b><br>1180 Alder Creek Lane,<br>Ridgefield, VA23001</div>
    <div class="foot"></div>
    <span class="btn-prev">Perview Now</span>
    <span class="fav"><svg width="18" height="17" viewBox="0 0 24 23"><path d="M12 0 15 8 24 8.5 17 14 19.5 23 12 18 4.5 23 7 14 0 8.5 9 8Z" fill="#f2b71a"/></svg>Add to Favorite</span>
  </article>

  <article class="abs card" style="top:861px">
    <div class="pic" role="img" aria-label="Photo of a green tractor with yellow wheels working in a field" style="top:20px;left:11px;background:linear-gradient(#5b82b8,#9fb0a0 40%,#3f7a2a 70%,#8a7a3c)"></div>
    <div class="col" style="left:173px;top:20px"><b>Title</b><br>Kestrel 4WD &amp; Commercial<br>Vehicles (107)</div>
    <div class="divider" style="left:345px;top:18px"></div>
    <div class="col" style="left:363px;top:16px"><b>Start Date / Time</b><br><span style="color:#222">Tue 09 April, 10:00 AM</span><br><b style="margin-top:8px">Location</b><br>1180 Alder Creek Lane,<br>Ridgefield, VA23001</div>
    <div class="foot" style="top:132px"></div>
    <span class="btn-prev" style="top:137px">Perview Now</span>
    <span class="fav" style="left:365px;top:139px"><svg width="18" height="17" viewBox="0 0 24 23"><path d="M12 0 15 8 24 8.5 17 14 19.5 23 12 18 4.5 23 7 14 0 8.5 9 8Z" fill="#f2b71a"/></svg>Add to Favorite</span>
  </article>
</main>

<footer class="abs footer">
  <p class="links">Home - Upcoming Auctions - Past Auctions - For Sale - Consignments &nbsp;- Highlights - &nbsp;Contact Us</p>
  <p class="contact">Phone: 14355501820, Email: info@tobwinenterprises.com</p>
  <div class="flogo"><i></i><div>Tobwin<small>ENTERPRISES</small></div></div>
  <div class="badges">
    <span style="width:28px;height:32px"></span>
    <span style="width:62px;height:30px;border-radius:4px"></span>
    <span style="width:62px;height:22px;border-radius:4px"></span>
    <span style="width:48px;height:48px;border-radius:50%"></span>
    <span style="width:100px;height:42px;border-radius:4px"></span>
  </div>
  <p class="copy">Copyright (C) Tobwin &nbsp;Enterprises. 2013 - 2014 . &nbsp;All Rights Reserved</p>
</footer>

</body>
</html>
```